New Business Card Design Project

Bloom of the Willow Wellness Clinic PLLC
Bloomofthewillowwc-example.com
Board Certified Nursing Coach in life, health, & wellness.
Hypnotherapy, weight loss & vitamin supplement injections, IV hydration.
Offering mobile clinics

```html
<!DOCTYPE html>
<html lang="en">
<head>
<meta charset="utf-8">
<title>Bloom of the Willow Wellness Clinic – Business Card</title>
<link rel="stylesheet" href="https://fonts.googleapis.com/css2?family=Montserrat:wght@600;800&family=Open+Sans:ital,wght@0,400;0,600;1,400&display=swap">
<style>
  :root {
    --page-bg: #2b2b2b;
    --card-bg: #1e1e1e;
    --ink: #f4f1ec;
    --muted: #d9d4cc;
    --orange: #f07a1c;
    --orange-soft: #f7a53a;
    --rule: #cfcac2;
  }
  * { box-sizing: border-box; margin: 0; padding: 0; }
  html, body { width: 1200px; height: 900px; overflow: hidden; }
  body {
    background: var(--page-bg);
    font-family: "Open Sans", Arial, sans-serif;
    color: var(--ink);
    display: flex;
    flex-direction: column;
    align-items: center;
    justify-content: center;
    gap: 28px;
  }
  .card {
    width: 680px;
    height: 389px;
    background: var(--card-bg);
    position: relative;
    overflow: hidden;
    box-shadow: 0 10px 30px rgba(0,0,0,.45);
  }

  /* Front */
  .front-brand {
    position: absolute;
    left: 60px; top: 90px;
    width: 230px;
    display: flex; flex-direction: column; align-items: center; gap: 18px;
  }
  .brand-dot {
    width: 110px; height: 110px; border-radius: 50%;
    background: var(--orange);
  }
  .brand-name {
    font-family: "Montserrat", Arial, sans-serif;
    font-weight: 800;
    color: var(--orange);
    font-size: 20px;
    line-height: 1.2;
    text-align: center;
    text-transform: uppercase;
    letter-spacing: 1px;
  }
  .divider {
    position: absolute; left: 0; top: 0; width: 680px; height: 389px;
  }
  .contact {
    position: absolute; left: 368px; top: 108px;
  }
  .person-name {
    font-family: "Montserrat", Arial, sans-serif;
    font-weight: 800; font-size: 24px;
    color: var(--orange);
    text-transform: uppercase;
  }
  .person-role { font-size: 18px; margin-bottom: 14px; }
  .address { font-size: 16px; line-height: 1.35; margin-bottom: 12px; }
  .contact-list { list-style: none; font-size: 16px; line-height: 1.55; }
  .contact-list li { display: flex; align-items: center; gap: 8px; }
  .contact-list svg { width: 16px; height: 16px; flex: none; }

  /* Back */
  .back { text-align: center; padding-top: 48px; }
  .back-title-row {
    display: flex; align-items: center; justify-content: center; gap: 18px;
  }
  .title-rule {
    width: 90px; height: 3px;
    background: linear-gradient(90deg, transparent, var(--orange));
  }
  .title-rule.right { background: linear-gradient(90deg, var(--orange), transparent); }
  .back-name {
    font-family: "Montserrat", Arial, sans-serif;
    font-weight: 800;
    color: var(--orange);
    font-size: 34px;
    letter-spacing: 4px;
    text-transform: uppercase;
    line-height: 1.15;
  }
  .back-sub {
    font-family: "Montserrat", Arial, sans-serif;
    font-weight: 800;
    color: var(--orange);
    font-size: 22px;
    letter-spacing: 5px;
    text-transform: uppercase;
    margin-top: 4px;
  }
  .services-heading {
    font-family: "Montserrat", Arial, sans-serif;
    font-weight: 800; font-size: 26px;
    color: var(--orange-soft);
    text-transform: uppercase;
    margin: 26px 0 12px;
  }
  .services { font-size: 17px; line-height: 1.5; color: var(--ink); }
  .services .dot { color: var(--orange); margin: 0 6px; }
</style>
</head>
<body>

  <section class="card front" aria-label="Business card front">
    <div class="front-brand">
      <div class="brand-dot"></div>
      <p class="brand-name">Bloom of the Willow</p>
    </div>
    <svg class="divider" viewBox="0 0 680 389" aria-hidden="true">
      <line x1="350" y1="80" x2="300" y2="320" stroke="var(--rule)" stroke-width="1.5"/>
    </svg>
    <div class="contact">
      <h1 class="person-name">Daniel Harper</h1>
      <p class="person-role">Managing Director</p>
      <p class="address">Your Address, City<br>State, Zip 0000</p>
      <ul class="contact-list">
        <li>
          <svg viewBox="0 0 16 16" aria-hidden="true"><path fill="var(--orange)" d="M3 1h3l1.5 4-2 1.2a9 9 0 0 0 4.3 4.3L11 8.5l4 1.5v3a2 2 0 0 1-2 2A12 12 0 0 1 1 3a2 2 0 0 1 2-2z"/></svg>
          044-555 010 246
        </li>
        <li>
          <svg viewBox="0 0 16 16" aria-hidden="true"><rect x="1" y="3" width="14" height="10" rx="1.5" fill="var(--orange)"/><path d="M1.5 4 8 9l6.5-5" fill="none" stroke="var(--card-bg)" stroke-width="1.3"/></svg>
          info@bloomwillow-example.com
        </li>
        <li>
          <svg viewBox="0 0 16 16" aria-hidden="true"><circle cx="8" cy="8" r="7" fill="var(--orange)"/><path d="M1 8h14M8 1c3 3 3 11 0 14M8 1c-3 3-3 11 0 14" fill="none" stroke="var(--card-bg)" stroke-width="1"/></svg>
          Bloomofthewillowwc-example.com
        </li>
      </ul>
    </div>
  </section>

  <section class="card back" aria-label="Business card back">
    <div class="back-title-row">
      <span class="title-rule"></span>
      <h2 class="back-name">Bloom of the Willow</h2>
      <span class="title-rule right"></span>
    </div>
    <p class="back-sub">Wellness Clinic</p>
    <h3 class="services-heading">Our Service</h3>
    <p class="services">
      <span class="dot">&#9679;</span>Board Certified Nursing Coach in life <span class="dot">&#9679;</span> health &amp; wellness.<br>
      <span class="dot">&#9679;</span>Hypnotherapy <span class="dot">&#9679;</span> weight loss &amp; vitamin supplement injections<br>
      <span class="dot">&#9679;</span>IV hydration <span class="dot">&#9679;</span> Offering mobile clinics
    </p>
  </section>

</body>
</html>
```